TK Drafting

Simple Design - Logo is done (from this site). Logo on one side - Back Side an image or outline of a house blue print - My name, phone, email, website url. Prefer the traditional Architectural style of letters -

Target Market(s)

Customers who need a floor plan redesigned for renovations or realtors who want a floor plan for marketing their listings

Industry/Entity Type

Architecture

Contact Information for Business Card

Colby Faust - Name
415-362-8840 - Phone
tkdraftingco@mailpost.example
www.tkdraftingco.example

Font styles to use
Other font styles liked:
• Architecture writing -

Colors
0555a3
3276b5
85acd3

Requirements
Must have
• Logo that is attached. I like an indigo blue color for the background or a royal blue - gray logo OR - white and clean with the logo on one side and the same color gray lettering on the other side
Nice to have
• some sort of image that shows a residential blue print. It may not be possible on this small of a card though.
Should not have
• Nothing cartoonish.

```html
<!DOCTYPE html>
<html lang="en">
<head>
<meta charset="utf-8">
<title>TK Drafting – Business Card</title>
<link rel="stylesheet" href="https://fonts.googleapis.com/css2?family=Open+Sans:wght@400;700&display=swap">
<style>
  :root {
    --page-bg: #e6ebf1;
    --royal: #0555a3;
    --mid-blue: #3276b5;
    --pale-blue: #85acd3;
    --ink: #ffffff;
  }
  * { margin: 0; padding: 0; box-sizing: border-box; }
  html, body {
    width: 1200px;
    height: 900px;
    overflow: hidden;
    background: var(--page-bg);
    font-family: "Open Sans", Arial, sans-serif;
  }
  .business-card {
    position: absolute;
    left: 75px;
    top: 150px;
    width: 1050px;
    height: 600px;
    background: var(--royal);
    color: var(--ink);
    overflow: hidden;
  }
  .blueprint-area {
    position: absolute;
    inset: 0;
    background: radial-gradient(ellipse at 30% 50%, var(--mid-blue) 0%, var(--royal) 70%);
  }
  .brand {
    position: absolute;
    left: 60px;
    top: 0;
    width: 400px;
    height: 600px;
    display: flex;
    align-items: center;
    justify-content: center;
    gap: 18px;
  }
  .brand-mark {
    width: 34px;
    height: 34px;
    background: var(--ink);
    flex: none;
  }
  .brand-name {
    font-size: 46px;
    font-weight: 700;
    color: var(--ink);
    white-space: nowrap;
  }
  .divider {
    position: absolute;
    left: 500px;
    top: 170px;
    width: 2px;
    height: 260px;
    background: var(--pale-blue);
  }
  .contact {
    position: absolute;
    left: 545px;
    top: 200px;
  }
  .contact-name {
    font-size: 32px;
    font-weight: 700;
    letter-spacing: 1px;
    text-transform: uppercase;
    margin-bottom: 26px;
  }
  .contact-list { list-style: none; }
  .contact-item {
    display: flex;
    align-items: center;
    gap: 12px;
    font-size: 25px;
    line-height: 40px;
    white-space: nowrap;
  }
  .contact-icon {
    width: 20px;
    height: 20px;
    flex: none;
    fill: var(--ink);
  }
</style>
</head>
<body>
  <section class="business-card">
    <div class="blueprint-area" role="img" aria-label="Faint residential floor plan blueprint behind the card content"></div>

    <div class="brand">
      <span class="brand-mark"></span>
      <span class="brand-name">TK Drafting</span>
    </div>

    <div class="divider"></div>

    <div class="contact">
      <h1 class="contact-name">Colby Faust</h1>
      <ul class="contact-list">
        <li class="contact-item">
          <svg class="contact-icon" viewBox="0 0 24 24" aria-hidden="true">
            <path d="M6.6 10.8a15.1 15.1 0 0 0 6.6 6.6l2.2-2.2c.3-.3.7-.4 1-.2 1.1.4 2.3.6 3.6.6.6 0 1 .4 1 1V20c0 .6-.4 1-1 1A17 17 0 0 1 3 4c0-.6.4-1 1-1h3.5c.6 0 1 .4 1 1 0 1.3.2 2.5.6 3.6.1.3 0 .7-.2 1z"/>
          </svg>
          415-362-8840
        </li>
        <li class="contact-item">
          <svg class="contact-icon" viewBox="0 0 24 24" aria-hidden="true">
            <path d="M2 5h20v14H2zM3.5 6.5 12 13l8.5-6.5z" fill-rule="evenodd"/>
          </svg>
          tkdraftingco@mailpost.example
        </li>
        <li class="contact-item">
          <svg class="contact-icon" viewBox="0 0 24 24" aria-hidden="true">
            <path d="M12 2a10 10 0 1 0 0 20 10 10 0 0 0 0-20zm0 2c.9 1.2 1.6 2.6 2 4h-4c.4-1.4 1.1-2.8 2-4zM4.3 14a8 8 0 0 1 0-4h3.4a16 16 0 0 0 0 4zm.8 2h3c.3 1.2.8 2.4 1.4 3.5A8 8 0 0 1 5.1 16zm3-8h-3a8 8 0 0 1 4.4-3.5C8.9 5.6 8.4 6.8 8.1 8zM12 20c-.9-1.2-1.6-2.6-2-4h4c-.4 1.4-1.1 2.8-2 4zm2.3-6H9.7a14 14 0 0 1 0-4h4.6a14 14 0 0 1 0 4zm.2 5.5c.6-1.1 1.1-2.300 1.4-3.5h3a8 8 0 0 1-4.4 3.5zm1.8-5.5a16 16 0 0 0 0-4h3.4a8 8 0 0 1 0 4z"/>
          </svg>
          www.tkdraftingco.example
        </li>
      </ul>
    </div>
  </section>
</body>
</html>
```